Veltrano - Mechanic/Collision Center Business Card

We're looking for a business card design for our mechanic/ collision repair shop.

Can be with colours or monochromatic.

See the attached files.

Many thanks

```html
<!DOCTYPE html>
<html lang="pt">
<head>
<meta charset="utf-8">
<title>Veltrano – Business Card</title>
<link rel="stylesheet" href="https://fonts.googleapis.com/css2?family=Alfa+Slab+One&family=Roboto+Condensed:wght@700&family=Ubuntu:wght@400;500&display=swap">
<style>
  :root {
    --backdrop: #2f6a86;
    --card-dark: #333132;
    --card-blue: #2e9fd9;
    --ink: #2d2d2f;
    --white: #ffffff;
    --accent-grey: #7d7e82;
  }
  * { margin: 0; padding: 0; box-sizing: border-box; }
  html, body { width: 1200px; height: 1200px; overflow: hidden; }
  body {
    background: var(--backdrop);
    position: relative;
    font-family: "Ubuntu", sans-serif;
  }
  .card {
    position: absolute;
    left: 160px;
    width: 880px;
    height: 503px;
    border-radius: 26px;
    overflow: hidden;
  }
  .card--back { top: 73px; background: var(--card-dark); }
  .card--front { top: 624px; background: var(--card-blue); color: var(--ink); }

  /* back side brand */
  .brand-back {
    position: absolute;
    left: 0; right: 0; top: 150px;
    display: flex; flex-direction: column; align-items: center; gap: 26px;
  }
  .brand-back .brand-dot {
    width: 96px; height: 96px; border-radius: 50%;
    background: var(--card-blue);
  }
  .brand-back .brand-name {
    font-family: "Roboto Condensed", sans-serif;
    font-weight: 700;
    font-size: 92px;
    letter-spacing: 2px;
    color: var(--white);
    line-height: 1;
  }

  /* front side */
  .person {
    position: absolute;
    left: 0; width: 378px; top: 128px;
    text-align: center;
  }
  .person-name {
    font-family: "Alfa Slab One", serif;
    font-size: 31px;
    letter-spacing: 1px;
    line-height: 1.1;
  }
  .person-phone {
    font-family: "Roboto Condensed", sans-serif;
    font-weight: 700;
    font-size: 33px;
    margin-top: 6px;
  }
  .brand-front {
    margin-top: 38px;
    display: flex; flex-direction: column; align-items: center; gap: 12px;
  }
  .brand-front .brand-dot {
    width: 48px; height: 48px; border-radius: 50%;
    background: var(--white);
  }
  .brand-front .brand-name {
    font-family: "Roboto Condensed", sans-serif;
    font-weight: 700;
    font-size: 44px;
    letter-spacing: 1px;
    color: var(--ink);
    line-height: 1;
  }
  .divider {
    position: absolute;
    left: 378px; top: 63px;
    width: 2px; height: 375px;
    background: var(--ink);
  }
  .company {
    position: absolute;
    left: 426px; top: 103px;
    font-family: "Alfa Slab One", serif;
    font-size: 28px;
    letter-spacing: .5px;
  }
  .contact-list {
    position: absolute;
    left: 410px; top: 160px;
    list-style: none;
  }
  .contact-item {
    display: flex; align-items: center;
    height: 49px;
    font-size: 26px;
    font-weight: 500;
  }
  .contact-item .icon {
    width: 40px; height: 34px; margin-right: 18px;
    display: flex; align-items: center; justify-content: center;
  }
  .contact-item .icon svg { display: block; }
  .contact-item--phone, .contact-item--postal {
    font-family: "Roboto Condensed", sans-serif;
    font-weight: 700;
    font-size: 28px;
    letter-spacing: .5px;
  }
</style>
</head>
<body>

<section class="card card--back" aria-label="Card back">
  <div class="brand-back">
    <span class="brand-dot"></span>
    <span class="brand-name">VELTRANO</span>
  </div>
</section>

<section class="card card--front" aria-label="Card front">
  <div class="person">
    <p class="person-name">RUI MATOS</p>
    <p class="person-phone">913472085</p>
    <div class="brand-front">
      <span class="brand-dot"></span>
      <span class="brand-name">VELTRANO</span>
    </div>
  </div>

  <div class="divider"></div>

  <p class="company">Veltrano, LDA</p>

  <ul class="contact-list">
    <li class="contact-item contact-item--phone">
      <span class="icon">
        <svg width="34" height="34" viewBox="0 0 34 34" fill="none" stroke="#fff" stroke-width="2.4">
          <circle cx="17" cy="17" r="15"/>
          <path d="M12 9c-2 1-3 3-2 6 1.5 4 4.5 7.5 8.5 9 2.5 1 4 0 5-1.5l-3-3-2.5 1.5c-2-1-3.5-3-4.5-5l1.8-2z" fill="#fff" stroke-linejoin="round"/>
        </svg>
      </span>
      214550192
    </li>
    <li class="contact-item contact-item--postal">
      <span class="icon">
        <svg width="40" height="30" viewBox="0 0 40 30" fill="#fff">
          <path d="M4 12c0-5 4-8 8-8h22c3 0 5 2 5 5v12H12V12c0-3-2-4-4-4s-4 1-4 4v16H2V12z"/>
          <rect x="22" y="10" width="3" height="9" fill="#2e9fd9"/>
          <rect x="22" y="10" width="8" height="3" fill="#2e9fd9"/>
        </svg>
      </span>
      1700-245 Lisboa
    </li>
    <li class="contact-item">
      <span class="icon">
        <svg width="24" height="30" viewBox="0 0 24 30" fill="none" stroke="#fff" stroke-width="2.4">
          <path d="M12 3a6 6 0 0 0-6 6c0 5 6 11 6 11s6-6 6-11a6 6 0 0 0-6-6z"/>
          <circle cx="12" cy="9" r="2"/>
          <ellipse cx="12" cy="25" rx="9" ry="3"/>
        </svg>
      </span>
      Rua das Oficinas, 14
    </li>
    <li class="contact-item">
      <span class="icon">
        <svg width="34" height="24" viewBox="0 0 34 24" fill="none" stroke="#fff" stroke-width="2.2">
          <rect x="2" y="3" width="30" height="18"/>
          <path d="M2 3l15 11 15-11M2 21l11-9M32 21l-11-9"/>
        </svg>
      </span>
      oficina@veltrano.pt
    </li>
    <li class="contact-item">
      <span class="icon">
        <svg width="30" height="30" viewBox="0 0 30 30" fill="none" stroke="#fff" stroke-width="2.2">
          <circle cx="15" cy="15" r="12"/>
          <ellipse cx="15" cy="15" rx="5" ry="12"/>
          <path d="M3 15h24"/>
        </svg>
      </span>
      www.veltrano.pt/oficina
    </li>
  </ul>
</section>

</body>
</html>
```